High End Business Card Design for Flooring Store

Looking for a new card design for our hardwood flooring company. We have no print budget for these and are open to cards made from wood, metal, cardstock with embossed print ... or any combination of these. No plastic.

We sell luxury products and I want the cards to reflect our image of quality and class.

Our contact information as such;
Employee Name
418 Colbrook Blvd.
Larkmoor, RV
K9R-3M5
(555) 214-3968
Employee email @velkaflooring.com

Target Market(s)

Home Builders

Contact Information for Business Card

Emnployee name, business contact information

```html
<!DOCTYPE html>
<html lang="en">
<head>
<meta charset="utf-8">
<title>Velka Flooring – Business Card</title>
<link href="https://fonts.googleapis.com/css2?family=Montserrat:wght@400;500&family=Outfit:wght@400;600&display=swap" rel="stylesheet">
<style>
  :root {
    --backdrop: #6f7275;
    --card: #ffffff;
    --brand-red: #9b2a24;
    --brand-gold: #e8b22e;
    --tagline-grey: #6d6e70;
    --ink: #231f20;
  }
  * { margin: 0; padding: 0; box-sizing: border-box; }
  html, body { width: 1200px; height: 1200px; overflow: hidden; }
  body { background: var(--backdrop); position: relative; font-family: "Outfit", sans-serif; color: var(--ink); }

  .card {
    position: absolute;
    left: 244px;
    width: 708px;
    height: 410px;
    background: var(--card);
    overflow: hidden;
  }
  .card--front { top: 130px; }
  .card--back { top: 644px; }

  /* Front */
  .front-lockup {
    position: absolute;
    left: 0; right: 0; top: 136px;
    display: flex; flex-direction: column; align-items: center;
  }
  .wordmark-row { display: flex; align-items: center; gap: 14px; }
  .brand-square { background: var(--brand-gold); }
  .wordmark {
    font-family: "Montserrat", sans-serif;
    font-weight: 500;
    color: var(--brand-red);
    line-height: 1;
  }
  .card--front .brand-square { width: 52px; height: 52px; }
  .card--front .wordmark { font-size: 95px; letter-spacing: 1px; }
  .tagline {
    font-family: "Montserrat", sans-serif;
    font-weight: 400;
    color: var(--tagline-grey);
    text-align: center;
    line-height: 1.1;
  }
  .card--front .tagline { font-size: 23px; margin-top: 4px; margin-left: 60px; }

  /* Back */
  .back-lockup {
    position: absolute; left: 44px; top: 40px;
    display: flex; flex-direction: column; align-items: center;
  }
  .card--back .wordmark-row { gap: 9px; }
  .card--back .brand-square { width: 26px; height: 26px; }
  .card--back .wordmark { font-size: 48px; }
  .card--back .tagline { font-size: 12px; margin-left: 30px; }

  .person-name {
    position: absolute; left: 49px; top: 256px;
    font-size: 25px; font-weight: 600; letter-spacing: 1.5px;
    color: var(--brand-red);
  }
  .person-role {
    position: absolute; left: 50px; top: 284px;
    font-size: 16.5px; letter-spacing: 0.5px;
  }
  .contact-rule {
    position: absolute; left: 48px; top: 313px;
    width: 617px; height: 1.5px; background: var(--ink);
  }
  .contact-list { position: absolute; list-style: none; font-size: 16px; }
  .contact-list li { display: flex; align-items: center; height: 25px; gap: 14px; white-space: nowrap; }
  .contact-list svg { fill: var(--brand-red); flex: none; }
  .contact-list--left { left: 50px; top: 332px; }
  .contact-list--right { right: 46px; top: 331px; text-align: right; }
  .contact-list--right li { justify-content: flex-end; }
</style>
</head>
<body>

<section class="card card--front">
  <div class="front-lockup">
    <div class="wordmark-row">
      <span class="brand-square"></span>
      <span class="wordmark">Velka</span>
    </div>
    <p class="tagline">Planchers &amp; Escaliers<br>Flooring &amp; Stairs</p>
  </div>
</section>

<section class="card card--back">
  <div class="back-lockup">
    <div class="wordmark-row">
      <span class="brand-square"></span>
      <span class="wordmark">Velka</span>
    </div>
    <p class="tagline">Planchers &amp; Escaliers<br>Flooring &amp; Stairs</p>
  </div>

  <h2 class="person-name">Owen Harlow</h2>
  <p class="person-role">Manager</p>
  <div class="contact-rule"></div>

  <ul class="contact-list contact-list--left">
    <li>
      <svg width="14" height="14" viewBox="0 0 24 24" aria-hidden="true"><path d="M6.6 2.5l3 .4 1 5-2.6 1.6c.9 2.6 2.9 4.9 5.4 6.3l1.8-2.4 4.9 1.3.2 3.1c-.2 1.6-1.7 2.6-3.3 2.4C9.5 19.1 3.9 12.6 3.6 5.9 3.5 4.1 4.8 2.6 6.6 2.5z"/></svg>
      <span>(555)214-3968</span>
    </li>
    <li>
      <svg width="16" height="12" viewBox="0 0 24 18" aria-hidden="true"><path d="M0 0h24v18H0z M2 2.5v.5l10 7 10-7v-.5z" fill-rule="evenodd"/></svg>
      <span>Info@velkaflooring.com</span>
    </li>
  </ul>

  <ul class="contact-list contact-list--right">
    <li>
      <span>www.velkaflooring.com</span>
      <svg width="15" height="15" viewBox="0 0 24 24" aria-hidden="true"><path d="M12 1a11 11 0 1 0 0 22 11 11 0 0 0 0-22zm0 3c1 1.5 1.7 3.5 1.9 6h-3.8C10.3 7.5 11 5.5 12 4zM8.1 10H4.3a8 8 0 0 1 5-5.5C8.6 6 8.2 8 8.1 10zm0 4c.1 2 .5 4 1.2 5.5a8 8 0 0 1-5-5.5zm2 0h3.8c-.2 2.5-.9 4.5-1.9 6-1-1.5-1.7-3.5-1.9-6zm5.8 0h3.8a8 8 0 0 1-5 5.5c.7-1.5 1.1-3.5 1.2-5.5zm0-4c-.1-2-.5-4-1.2-5.5a8 8 0 0 1 5 5.5z"/></svg>
    </li>
    <li>
      <span>418 Colbrook Blvd. Larkmoor, RV K9R 3M5</span>
      <svg width="13" height="17" viewBox="0 0 18 24" aria-hidden="true"><path d="M9 0a9 9 0 0 0-9 9c0 6.5 9 15 9 15s9-8.5 9-15a9 9 0 0 0-9-9zm0 5a4 4 0 1 1 0 8 4 4 0 0 1 0-8z" fill-rule="evenodd"/></svg>
    </li>
  </ul>
</section>

</body>
</html>
```